inspirational business card

I want to use the Vector on Pixmarra.com (number 61827405) and I will purchase the vector to send it to the designer once the general concept is approved. You can download it for free for a one time use on providing a design for this request.
Within the vector, insert:
Denise Halvorsen
Guidance and Cooperative

I prefer a vertical card but do not require vertical.

Contact info:

Denise Halvorsen, J.D.
Collaborative Lawyer
Certified Divorce Coach
Mediation Coach
PHONE 641/382-4076
EMAIL: dhrt@quelvo.net

Website: Guidanceandcooperative.com
Settlementcourse.com

I like greens, blue and grey. I do not want black font, and would like the font to be legible without needing perfect reading vision (no super small font).
I would like the overall theme to convey growth and nurturance.
I like the vector I selected because of the growth and light portrayed.
Not too frilly or too bold. I would like to to appeal to both sexes.

Target Market(s)

Generally professional women 35-60

Industry/Entity Type

Attorney

Font styles to use
Serif
Sans Serif

Colors
acd136
cadf82
fbf289
9d9d9d

Requirements
Must have
• My project does not need to have my photo but you could use it if you want
Nice to have
• Vertical
• I like rounded edges on the cards
Should not have
• I do not like my name appearing two times in close proximity. I'm not a flowery person.

```html
<!DOCTYPE html>
<html lang="en">
<head>
<meta charset="utf-8">
<title>Denise Halvorsen — Business Card</title>
<link rel="stylesheet" href="https://fonts.googleapis.com/css2?family=Arimo:ital,wght@0,400;0,700;1,400&display=swap">
<style>
  :root {
    --backdrop: #c6c6c8;
    --card-white: #f3f3f3;
    --card-blue: #2e8bd3;
    --brand-green: #3f7d22;
    --leaf-light: #acd136;
    --leaf-mid: #6aa83a;
    --name-blue: #1a5cb8;
    --title-blue: #2a6cc6;
    --label-grey: #8e8e8e;
    --value-grey: #9d9d9d;
    --sky-light: #7fc0ee;
    --white: #ffffff;
  }
  * { box-sizing: border-box; margin: 0; padding: 0; }
  html, body {
    width: 1103px;
    height: 1200px;
    overflow: hidden;
    background: var(--backdrop);
    font-family: "Arimo", Arial, sans-serif;
  }
  .stage {
    width: 1103px;
    height: 1200px;
    display: flex;
    align-items: center;
    justify-content: center;
    gap: 60px;
  }
  .card {
    width: 400px;
    height: 700px;
    border-radius: 14px;
    position: relative;
    box-shadow: 0 10px 30px rgba(0,0,0,0.18);
  }
  .card--front { background: var(--card-white); }
  .card--back { background: var(--card-blue); }

  .brand {
    position: absolute;
    left: 0; right: 0;
    display: flex;
    flex-direction: column;
    align-items: center;
    text-align: center;
  }
  .card--front .brand { top: 90px; }
  .card--back .brand { top: 210px; }

  .brand-disc {
    width: 170px;
    height: 170px;
    border-radius: 50%;
  }
  .card--front .brand-disc {
    background: radial-gradient(circle at 45% 40%, var(--leaf-light), var(--leaf-mid) 70%, var(--brand-green));
  }
  .card--back .brand-disc {
    background: radial-gradient(circle at 45% 40%, #eef7fd, var(--sky-light) 75%);
  }
  .brand-name {
    margin-top: 18px;
    font-weight: 700;
    font-size: 28px;
    line-height: 1.2;
    letter-spacing: -0.3px;
  }
  .card--front .brand-name { color: var(--brand-green); }
  .card--back .brand-name { color: var(--white); }

  .details {
    position: absolute;
    left: 0; right: 0;
    top: 370px;
    text-align: center;
  }
  .person-name {
    font-weight: 700;
    font-size: 30px;
    color: var(--name-blue);
  }
  .roles { margin-top: 10px; }
  .role {
    font-size: 19px;
    color: var(--title-blue);
    line-height: 1.3;
  }
  .contact {
    list-style: none;
    margin-top: 22px;
    font-size: 15px;
    line-height: 1.8;
  }
  .contact-label {
    font-weight: 700;
    color: var(--label-grey);
    margin-right: 4px;
  }
  .contact-value {
    font-style: italic;
    color: var(--value-grey);
  }
  .contact-value--block { display: block; }
</style>
</head>
<body>
<main class="stage">
  <section class="card card--front">
    <div class="brand">
      <div class="brand-disc" role="img" aria-label="Tree of light emblem in greens"></div>
      <div class="brand-name">Guidance and Cooperative</div>
    </div>
    <div class="details">
      <h1 class="person-name">Denise Halvorsen, J.D.</h1>
      <div class="roles">
        <p class="role">Collaborative Lawyer</p>
        <p class="role">Certified Divorce Coach</p>
        <p class="role">Mediation Coach</p>
      </div>
      <ul class="contact">
        <li><span class="contact-label">PHONE:</span><span class="contact-value">641/382-4076</span></li>
        <li><span class="contact-label">EMAIL:</span><span class="contact-value">dhrt@quelvo.net</span></li>
        <li><span class="contact-label">WEBSITE:</span>
          <span class="contact-value contact-value--block">Guidanceandcooperative.com</span>
          <span class="contact-value contact-value--block">Settlementcourse.com</span>
        </li>
      </ul>
    </div>
  </section>

  <section class="card card--back">
    <div class="brand">
      <div class="brand-disc" role="img" aria-label="Tree of light emblem in pale blues"></div>
      <div class="brand-name">Guidance and Cooperative<br>Denise Halvorsen</div>
    </div>
  </section>
</main>
</body>
</html>
```